furnace plenum sticker

This sticker is left at every job above the furnace or on the duct work connected to the furnace.
It needs to be bold so that when homeowner is at the furnace during a break down they see it. Phone number and what we do needs to be prominate. It is our calling card for service.
Sticker needs to look corporate and professional.

New logo (attached) must be incorporated into sticker.

Current sticker attached
Size
8.5 inches x 5.5 inches

Target Market(s)

residential home owners

Industry/Entity Type

Work

Colors
ec1f27

Requirements
Must have
• Our new current logo attached

```html
<!DOCTYPE html>
<html lang="en">
<head>
<meta charset="utf-8">
<title>Northfield Heating and Air Conditioning – Furnace Sticker</title>
<link href="https://fonts.googleapis.com/css2?family=Lato:wght@400;700;900&display=swap" rel="stylesheet">
<style>
  :root {
    --brand-red: #ec1f27;
    --ink: #111111;
    --band: #000000;
    --paper: #ffffff;
    --backdrop: #ebebeb;
    --on-band: #ffffff;
  }
  * { box-sizing: border-box; margin: 0; padding: 0; }
  html, body {
    width: 1200px;
    height: 1150px;
    overflow: hidden;
    background: var(--backdrop);
  }
  body { position: relative; font-family: "Lato", sans-serif; }

  .sticker {
    position: absolute;
    left: 50px;
    top: 244px;
    width: 1100px;
    height: 662px;
    background: var(--paper);
    overflow: hidden;
  }
  .sticker-shapes {
    position: absolute;
    inset: 0;
    width: 1100px;
    height: 662px;
  }

  .brand {
    position: absolute;
    left: 0;
    width: 100%;
    text-align: center;
    font-family: "Lato", sans-serif;
  }
  .brand-name {
    top: 112px;
    font-weight: 900;
    font-size: 92px;
    line-height: 1;
    letter-spacing: 1px;
    color: var(--brand-red);
  }
  .brand-tagline {
    top: 194px;
    font-weight: 900;
    font-size: 34px;
    line-height: 1;
    color: var(--ink);
  }

  .services {
    position: absolute;
    left: 0;
    width: 100%;
    list-style: none;
    display: flex;
    justify-content: center;
    gap: 44px;
    font-size: 31px;
    font-weight: 400;
    color: var(--ink);
    line-height: 1;
  }
  .services-row-1 { top: 302px; }
  .services-row-2 { top: 359px; }
  .service { display: flex; align-items: center; gap: 12px; }
  .service-bullet {
    width: 22px;
    height: 22px;
    border-radius: 50%;
    background: var(--brand-red);
    flex: none;
  }

  .contact {
    position: absolute;
    top: 530px;
    color: var(--on-band);
    line-height: 1;
  }
  .contact-left { right: 582px; text-align: right; }
  .contact-right { left: 577px; text-align: left; }
  .contact-phone {
    display: block;
    font-weight: 900;
    font-size: 44px;
    letter-spacing: 2px;
  }
  .contact-area {
    display: block;
    margin-top: 8px;
    font-weight: 700;
    font-size: 27px;
    letter-spacing: 1.5px;
  }
  .contact-left .contact-area { padding-right: 0; }
  .contact-divider {
    position: absolute;
    left: 548px;
    top: 505px;
    width: 5px;
    height: 112px;
    background: var(--brand-red);
  }
</style>
</head>
<body>
  <main class="sticker">
    <svg class="sticker-shapes" viewBox="0 0 1100 662" aria-hidden="true">
      <path class="accent-swoosh" fill="var(--brand-red)"
            d="M40,540 Q550,324 1060,540 Q550,352 40,540 Z"/>
      <path class="contact-band" fill="var(--band)"
            d="M20,560 Q550,360 1080,560 L1080,648 L20,648 Z"/>
    </svg>

    <h1 class="brand brand-name">NORTHFIELD</h1>
    <p class="brand brand-tagline">HEATING AND AIR CONDITIONING</p>

    <ul class="services services-row-1">
      <li class="service"><span class="service-bullet"></span>24 Hours Service</li>
      <li class="service"><span class="service-bullet"></span>Repairs &amp; Installations</li>
    </ul>
    <ul class="services services-row-2">
      <li class="service"><span class="service-bullet"></span>We Service All Makes &amp; Models.</li>
    </ul>

    <div class="contact contact-left">
      <span class="contact-phone">905-555-0147</span>
      <span class="contact-area">Burlington / Hamilton</span>
    </div>
    <div class="contact-divider"></div>
    <div class="contact contact-right">
      <span class="contact-phone">905-555-0182</span>
      <span class="contact-area">Oakville / Milton</span>
    </div>
  </main>
</body>
</html>
```